Business Card Design Project

Doctor, Pain Management. Need a new business card design with appointment info on the back. New address is 18 Birchwood Court, Suite 304, Holloway, NJ 07519. Right now I believe the rest of the information is staying the same.

```html
<!DOCTYPE html>
<html lang="en">
<head>
<meta charset="utf-8">
<title>Steady Relief Care – Business Card</title>
<link href="https://fonts.googleapis.com/css2?family=Montserrat:ital,wght@0,400;0,500;0,700;1,700&display=swap" rel="stylesheet">
<style>
  :root{
    --teal:#41aba4;
    --ink:#5b5f62;
    --rule:#9a9ea0;
    --paper:#f4f4f4;
    --bg:#e9e9e9;
  }
  *{box-sizing:border-box;margin:0;padding:0}
  html,body{width:1200px;height:1189px;overflow:hidden;background:var(--bg);font-family:"Montserrat",sans-serif;color:var(--ink)}
  .card{position:absolute;left:110px;width:980px;height:560px;background:var(--paper);box-shadow:0 4px 14px rgba(0,0,0,.12);overflow:hidden}
  .card--back{top:24px}
  .card--front{top:606px}

  /* back */
  .back-header{position:absolute;left:0;top:0;width:100%;height:118px;background:var(--teal);display:flex;align-items:center;justify-content:space-between;padding:0 56px;color:#fff}
  .brand{display:flex;align-items:center;gap:18px}
  .brand-dot{width:62px;height:62px;border:6px solid currentColor;border-radius:50%}
  .brand-name{font-weight:700;font-size:32px;letter-spacing:.5px;text-transform:uppercase}
  .header-contact{text-align:right}
  .header-phone{font-weight:700;font-size:34px;letter-spacing:1px}
  .header-web{font-weight:500;font-size:17px;letter-spacing:.5px;margin-top:2px}
  .appt-title{position:absolute;top:150px;left:0;width:100%;text-align:center;color:var(--teal);font-weight:700;font-style:italic;font-size:21px;letter-spacing:.5px}
  .field{position:absolute;display:flex;align-items:flex-end;font-style:italic;font-size:20px;color:var(--ink)}
  .field span{margin-right:12px}
  .field i{flex:1;border-bottom:1.5px solid var(--rule);height:20px}
  .field--for{left:56px;top:200px;width:868px}
  .field--date{left:56px;top:262px;width:540px}
  .field--time{left:620px;top:262px;width:304px}
  .days{position:absolute;left:56px;top:340px;width:868px;display:flex;justify-content:space-between;font-size:20px}
  .day{display:flex;align-items:center;gap:8px}
  .day b{display:inline-block;width:30px;height:26px;border:2px solid var(--teal)}
  .back-note{position:absolute;left:56px;right:56px;top:440px;text-align:center;color:var(--teal);font-weight:700;font-style:italic;font-size:19px}

  /* front */
  .front-logo{position:absolute;left:70px;top:120px;width:380px;display:flex;flex-direction:column;align-items:center;color:var(--teal);gap:22px}
  .front-logo .brand-dot{width:90px;height:90px;border-width:8px}
  .front-logo .brand-name{font-size:34px;text-align:center}
  .regions{position:absolute;left:70px;width:380px;top:400px;text-align:center;font-size:20px;letter-spacing:2px}
  .divider{position:absolute;left:490px;top:90px;width:1.5px;height:320px;background:#bdbfc0}
  .details{position:absolute;left:530px;top:120px;width:420px}
  .person-name{font-weight:700;font-size:28px;color:var(--ink)}
  .person-role{color:var(--teal);font-size:20px;margin-top:4px}
  .address{font-size:18px;margin-top:26px;line-height:1.45}
  .contact{list-style:none;margin-top:16px;font-size:18px;line-height:1.6}
  .contact li{display:flex;align-items:center;gap:12px}
  .contact svg{width:18px;height:18px;flex:none}
  .front-band{position:absolute;left:0;bottom:0;width:100%;height:16px;background:var(--teal)}
</style>
</head>
<body>

<section class="card card--back">
  <header class="back-header">
    <div class="brand">
      <span class="brand-dot"></span>
      <span class="brand-name">Steady Relief Care</span>
    </div>
    <div class="header-contact">
      <div class="header-phone">555.201.4830</div>
      <div class="header-web">www.steadyreliefcare.com</div>
    </div>
  </header>
  <h2 class="appt-title">YOUR NEXT APPOINTMENT</h2>
  <div class="field field--for"><span>For</span><i></i></div>
  <div class="field field--date"><span>Date</span><i></i></div>
  <div class="field field--time"><span>Time</span><i></i></div>
  <div class="days">
    <span class="day">Mon <b></b></span>
    <span class="day">Tue <b></b></span>
    <span class="day">Wed <b></b></span>
    <span class="day">Thur <b></b></span>
    <span class="day">Fri <b></b></span>
    <span class="day">Sat <b></b></span>
    <span class="day">Sun <b></b></span>
  </div>
  <p class="back-note">If you are unable to keep your appointment, please contact us as soon as possible.</p>
</section>

<section class="card card--front">
  <div class="front-logo">
    <span class="brand-dot"></span>
    <span class="brand-name">Steady Relief Care</span>
  </div>
  <p class="regions">New Jersey | New York</p>
  <div class="divider"></div>
  <div class="details">
    <h1 class="person-name">Lena Marlow, M.D., Ph.D</h1>
    <p class="person-role">Board Certified Anesthesiologist</p>
    <p class="address">18 Birchwood Court, Suite 304<br>Holloway, NJ 07519</p>
    <ul class="contact">
      <li><svg viewBox="0 0 24 24" fill="none" stroke="#5b5f62" stroke-width="2"><path d="M5 3h4l2 5-3 2a12 12 0 0 0 6 6l2-3 5 2v4a2 2 0 0 1-2 2A18 18 0 0 1 3 5a2 2 0 0 1 2-2z"/></svg>555.201.4830</li>
      <li><svg viewBox="0 0 24 24" fill="none" stroke="#5b5f62" stroke-width="2"><rect x="4" y="9" width="16" height="11" rx="1"/><path d="M7 9V4h10v5M8 14h8"/></svg>555.201.4831</li>
      <li><svg viewBox="0 0 24 24" fill="none" stroke="#5b5f62" stroke-width="2"><rect x="3" y="5" width="18" height="14" rx="1"/><path d="M3 6l9 7 9-7"/></svg>restwell.office@mail.com</li>
    </ul>
  </div>
  <div class="front-band"></div>
</section>

</body>
</html>
```